New Brand - Website Design (4 Pages)

We are launching a new brand for electronic cigarettes. We already have logo and packaging done and would like a web design to go with it.

We are interested in the following deliverables:

1) Home Page Design
2) Check Out Design
3) How it Works Page
4) Secondary Template Page Design

Looking for a 60s modern look and something that is consistent with our logo and packaging.

Industry/Entity Type

Electronic

Requirements
Must have
• Consistent with logo and packaging (Use Logo Attached)
White background

Example (Functionality & Design): http://www.torvex.co.uk/
Example (Design): http://www.quillharbor.com/

We want the design more like quillharbor but the functionality the same as torvex.

Top Bar: Pebble Arcs Kits; Cartridge Refills; How it Works; Contact; My Account; Checkout
Should not have
• Stock List or Search Bar or Newsletter Signup

```html
<!DOCTYPE html>
<html lang="en">
<head>
<meta charset="utf-8">
<title>Pebble Arcs — Home</title>
<link href="https://fonts.googleapis.com/css2?family=Open+Sans:wght@400;600;700;800&family=Oswald:wght@400;500;600&display=swap" rel="stylesheet">
<style>
:root{
  --teal:#1db4c6;
  --teal-dark:#128d9c;
  --ink:#2d3a44;
  --muted:#7b8790;
  --line:#e3e7ea;
  --soft:#f1f3f4;
  --footer:#3b4046;
  --footer-deep:#2a2e32;
  --white:#ffffff;
}
*{box-sizing:border-box;margin:0;padding:0}
html,body{width:829px;height:1200px;overflow:hidden;background:var(--white)}
body{font-family:"Open Sans",Arial,sans-serif;color:var(--ink);position:relative}
a{color:inherit;text-decoration:none}
ul{list-style:none}

/* header */
.site-header{position:absolute;top:0;left:0;width:829px;height:58px;border-bottom:3px solid var(--teal);background:var(--white)}
.brand{position:absolute;left:22px;top:12px;display:flex;align-items:center;gap:8px}
.brand-mark{width:30px;height:30px;background:var(--teal)}
.brand-name{font-family:"Open Sans",sans-serif;font-weight:800;font-size:20px;color:var(--teal);letter-spacing:.5px}
.account-links{position:absolute;right:92px;top:6px;font-size:8px;color:var(--muted)}
.cart-tab{position:absolute;right:14px;top:0;width:74px;height:18px;background:var(--ink);color:var(--white);font-size:7.5px;font-weight:700;text-align:center;line-height:18px;text-transform:uppercase}
.main-nav{position:absolute;right:16px;top:30px;display:flex;gap:18px;font-size:10.5px;color:var(--teal);font-weight:600}

/* hero */
.hero{position:absolute;top:61px;left:0;width:829px;height:274px;overflow:hidden}
.hero-photo{position:absolute;inset:0;background:linear-gradient(100deg,#6b3d22 0%,#c9793a 35%,#e0a76a 55%,#5a3321 80%,#2b1a13 100%)}
.hero-panel{position:absolute;left:0;top:0}
.hero-product{position:absolute;left:40px;top:62px;width:160px;height:140px;background:linear-gradient(160deg,#f4f4f4 0%,#d8d8d8 55%,#b5252f 56%,#8e1a22 100%);transform:rotate(-6deg)}
.hero-copy{position:absolute;right:46px;top:62px;text-align:right;color:var(--white)}
.hero-title{font-family:"Oswald",sans-serif;font-weight:600;font-size:30px;line-height:1;letter-spacing:.5px}
.hero-sub{font-family:"Oswald",sans-serif;font-size:22px;font-weight:400;margin-top:2px}
.hero-line{font-size:19px;line-height:1.1;margin-top:4px;max-width:220px;margin-left:auto}
.hero-price{font-family:"Oswald",sans-serif;font-size:24px;font-weight:500;margin-top:8px}
.btn{display:inline-block;background:var(--teal);color:var(--white);font-weight:700;text-transform:uppercase}
.hero-btn{margin-top:8px;padding:6px 16px;font-size:13px;border-radius:2px}
.hero-dots{position:absolute;right:22px;bottom:10px;display:flex;gap:5px}
.dot{width:7px;height:7px;border-radius:50%;background:rgba(255,255,255,.55)}
.dot.is-active{background:var(--white)}

/* usp strip */
.usp{position:absolute;top:335px;left:0;width:829px;height:112px;border-bottom:1px solid var(--line)}
.usp-flag{position:absolute;left:0;top:0}
.usp-flag-text{position:absolute;left:14px;top:30px;color:var(--white);font-family:"Oswald",sans-serif;text-align:center;line-height:1}
.usp-flag-text small{display:block;font-size:11px;letter-spacing:1px}
.usp-flag-text strong{display:block;font-size:22px;font-weight:600}
.usp-item{position:absolute;top:30px;width:200px;display:flex;gap:10px;align-items:flex-start}
.usp-item h3{font-size:15px;font-weight:700;color:var(--teal-dark)}
.usp-item p{font-size:8.5px;color:var(--muted)}
.usp-icon{width:24px;height:24px;border-radius:50%;background:var(--teal-dark);flex:none;display:flex;align-items:center;justify-content:center;margin-top:2px}
.usp-divider{position:absolute;top:22px;width:1px;height:60px;background:var(--line)}

/* flavours */
.flavours{position:absolute;top:460px;left:0;width:829px;height:240px}
.section-title{text-align:center;font-size:15px;color:var(--teal);font-weight:600;position:relative}
.section-title::before,.section-title::after{content:"";position:absolute;top:50%;width:300px;height:1px;background:var(--line)}
.section-title::before{left:40px}
.section-title::after{right:40px}
.carousel-arrow{position:absolute;top:95px;width:24px;height:24px;border-radius:50%;background:var(--teal);display:flex;align-items:center;justify-content:center}
.flavour-card{position:absolute;top:34px;width:140px;border:1px solid var(--line);background:var(--white)}
.flavour-photo{height:80px}
.flavour-body{padding:6px 7px 8px}
.flavour-body h4{font-size:9px;color:var(--teal);font-weight:700}
.flavour-body p{font-size:6.5px;color:var(--muted);line-height:1.35;margin-top:2px}
.flavour-foot{display:flex;justify-content:space-between;align-items:center;margin-top:6px;font-size:6.5px;font-weight:700}
.carousel-dots{position:absolute;top:218px;left:0;width:829px;display:flex;justify-content:center;gap:5px}
.carousel-dots .dot{background:#c9d0d4}
.carousel-dots .dot.is-active{background:var(--teal)}

/* info */
.info{position:absolute;top:710px;left:0;width:829px;height:172px;background:var(--soft);padding:18px 20px 0}
.info-col{position:absolute;top:18px;width:380px}
.info-col h2{font-size:13px;font-weight:800;color:var(--teal);text-transform:uppercase;padding-bottom:5px;border-bottom:1px solid #d6dcdf}
.info-col p{font-size:7.5px;line-height:1.5;color:var(--muted);margin-top:7px}

/* footer */
.site-footer{position:absolute;top:882px;left:0;width:829px;height:284px;background:var(--footer);color:#c5cbd0}
.footer-col{position:absolute;top:24px;width:180px}
.footer-col h5{font-size:9.5px;font-weight:700;color:var(--teal);text-transform:uppercase;margin-bottom:10px}
.footer-col li{font-size:8px;margin-bottom:6px}
.field{width:150px;height:16px;background:var(--white);margin-bottom:6px;border-radius:1px}
.login-btn{padding:4px 12px;font-size:7.5px;border-radius:2px}
.social{position:absolute;right:24px;top:228px;display:flex;gap:6px}
.social span{width:20px;height:20px;border-radius:50%;background:#5b6269}
.copyright{position:absolute;top:1166px;left:0;width:829px;height:34px;background:var(--footer-deep);color:#9aa3aa;font-size:8px;line-height:34px;padding-left:20px}
</style>
</head>
<body>

<header class="site-header">
  <a class="brand" href="#"><span class="brand-mark"></span><span class="brand-name">Pebble Arcs</span></a>
  <div class="account-links">Sign In | Login | Registration</div>
  <a class="cart-tab" href="#">Shopping Cart</a>
  <nav class="main-nav">
    <a href="#">Pebble Arcs Kits</a>
    <a href="#">Cartridge Refills</a>
    <a href="#">How it Works</a>
    <a href="#">Contact</a>
  </nav>
</header>

<section class="hero">
  <div class="hero-photo" role="img" aria-label="Concert crowd with raised hands under warm stage lights"></div>
  <svg class="hero-panel" width="300" height="274" viewBox="0 0 300 274">
    <polygon points="0,0 290,0 175,274 0,274" fill="#1db4c6"/>
  </svg>
  <div class="hero-product" role="img" aria-label="Pebble Arcs starter kit box"></div>
  <div class="hero-copy">
    <div class="hero-title">PEBBLE ARCS</div>
    <div class="hero-sub">Freedom</div>
    <div class="hero-line">Everything you need and more</div>
    <div class="hero-price">$ 55.75</div>
    <a class="btn hero-btn" href="#">Read More</a>
  </div>
  <div class="hero-dots"><span class="dot is-active"></span><span class="dot"></span><span class="dot"></span><span class="dot"></span></div>
</section>

<section class="usp">
  <svg class="usp-flag" width="132" height="112" viewBox="0 0 132 112">
    <polygon points="0,0 110,0 132,56 110,112 0,112" fill="#1db4c6"/>
  </svg>
  <div class="usp-flag-text"><small>WHY</small><strong>PEBBLE<br>ARCS</strong></div>

  <div class="usp-item" style="left:160px">
    <div><h3>Money Back</h3><p>30 Days Money Back Promise</p></div>
    <span class="usp-icon"><svg width="12" height="12" viewBox="0 0 12 12"><text x="6" y="10" font-size="10" font-weight="700" fill="#fff" text-anchor="middle" font-family="Open Sans,sans-serif">£</text></svg></span>
  </div>
  <span class="usp-divider" style="left:378px"></span>
  <div class="usp-item" style="left:400px">
    <div><h3>Free Shipping</h3><p>On Orders over $30</p></div>
    <span class="usp-icon"><svg width="14" height="10" viewBox="0 0 14 10"><rect x="0" y="1" width="8" height="6" fill="#fff"/><rect x="8" y="3" width="4" height="4" fill="#fff"/><circle cx="3" cy="8.5" r="1.5" fill="#fff"/><circle cx="10" cy="8.5" r="1.5" fill="#fff"/></svg></span>
  </div>
  <span class="usp-divider" style="left:598px"></span>
  <div class="usp-item" style="left:615px">
    <span class="usp-icon"><svg width="12" height="12" viewBox="0 0 12 12"><polyline points="2,6 5,9 10,3" fill="none" stroke="#fff" stroke-width="2"/></svg></span>
    <div><h3>1 year Warranty</h3><p>For your peace of Mind</p></div>
  </div>
</section>

<section class="flavours">
  <h2 class="section-title">Flavour</h2>
  <a class="carousel-arrow" href="#" style="left:58px"><svg width="10" height="10" viewBox="0 0 10 10"><polygon points="7,1 2,5 7,9" fill="#fff"/></svg></a>
  <a class="carousel-arrow" href="#" style="left:746px"><svg width="10" height="10" viewBox="0 0 10 10"><polygon points="3,1 8,5 3,9" fill="#fff"/></svg></a>

  <article class="flavour-card" style="left:256px">
    <div class="flavour-photo" role="img" aria-label="Fresh red cherries" style="background:linear-gradient(135deg,#8f1020,#d1283a 50%,#5e0a14)"></div>
    <div class="flavour-body">
      <h4>Sweet Cherry</h4>
      <p>Rich dark cherry notes with a smooth sweet finish in every draw.</p>
      <div class="flavour-foot"><span>READ MORE</span><svg width="12" height="10" viewBox="0 0 12 10"><path d="M0 1h2l2 6h6l1-4H3" fill="none" stroke="#1db4c6" stroke-width="1.2"/><circle cx="5" cy="9" r="1" fill="#1db4c6"/><circle cx="9" cy="9" r="1" fill="#1db4c6"/></svg></div>
    </div>
  </article>
  <article class="flavour-card" style="left:410px">
    <div class="flavour-photo" role="img" aria-label="Cinnamon sticks" style="background:linear-gradient(135deg,#7a4424,#b97a4a 50%,#e9dccb)"></div>
    <div class="flavour-body">
      <h4>Cinnamon</h4>
      <p>Warm spiced cinnamon blended with a soft vanilla base for depth.</p>
      <div class="flavour-foot"><span>READ MORE</span><svg width="12" height="10" viewBox="0 0 12 10"><path d="M0 1h2l2 6h6l1-4H3" fill="none" stroke="#1db4c6" stroke-width="1.2"/><circle cx="5" cy="9" r="1" fill="#1db4c6"/><circle cx="9" cy="9" r="1" fill="#1db4c6"/></svg></div>
    </div>
  </article>
  <article class="flavour-card" style="left:564px">
    <div class="flavour-photo" role="img" aria-label="Dried tobacco leaves" style="background:linear-gradient(135deg,#5c3a1c,#a06a34 50%,#6e4522)"></div>
    <div class="flavour-body">
      <h4>Classic Tobacco</h4>
      <p>A mellow roasted tobacco blend with a clean and light aftertaste.</p>
      <div class="flavour-foot"><span>READ MORE</span><svg width="12" height="10" viewBox="0 0 12 10"><path d="M0 1h2l2 6h6l1-4H3" fill="none" stroke="#1db4c6" stroke-width="1.2"/><circle cx="5" cy="9" r="1" fill="#1db4c6"/><circle cx="9" cy="9" r="1" fill="#1db4c6"/></svg></div>
    </div>
  </article>

  <div class="carousel-dots"><span class="dot is-active"></span><span class="dot"></span><span class="dot"></span></div>
</section>

<section class="info">
  <div class="info-col" style="left:20px">
    <h2>About Us</h2>
    <p>Pebble Arcs was created for people who want a cleaner, simpler way to enjoy the moments that matter. Every kit is designed, tested and packed with care so it works straight from the box, wherever your day takes you.</p>
    <p>We stand behind every product with honest advice, fast delivery and a full year of warranty cover on all of our starter kits.</p>
  </div>
  <div class="info-col" style="left:429px">
    <h2>Pebble Arc Cartridge Refills</h2>
    <p>Our cartridge refills come in a growing range of flavours and strengths, each one sealed for freshness and made to fit every Pebble Arcs battery. Order in packs of five or ten and save more as you stock up.</p>
    <p>Not sure where to start? Try a mixed flavour pack and find the taste that suits you best before you commit.</p>
  </div>
</section>

<footer class="site-footer">
  <div class="footer-col" style="left:30px">
    <h5>Our Products</h5>
    <ul><li>Starter Kits</li><li>Cartridge Refills</li><li>Batteries</li><li>Accessories</li></ul>
  </div>
  <div class="footer-col" style="left:228px">
    <h5>About Pebble Arc</h5>
    <ul><li>How it Works</li><li>Frequently Asked</li><li>Our Story</li><li>Contact Us</li></ul>
  </div>
  <div class="footer-col" style="left:428px">
    <h5>Ordering Information</h5>
    <ul><li>Delivery Information</li><li>Returns Policy</li><li>Terms &amp; Conditions</li><li>Privacy Policy</li></ul>
  </div>
  <div class="footer-col" style="left:628px">
    <h5>My Account</h5>
    <div class="field"></div>
    <div class="field"></div>
    <a class="btn login-btn" href="#">Login</a>
  </div>
  <div class="social"><span></span><span></span><span></span><span></span></div>
</footer>
<div class="copyright">Copyright © 2015 2014 All Rights Reserved</div>

</body>
</html>
```